Business Card Design Project

A business card for a new company in Ontario Canada called Sketch for Growth. It is a consulting company which uses Brixel as the medium for facilitation.

The target market is for senior leaders in healthcare and social services.

Industry/Entity Type

Healthcare

Requirements
Must have
• The name Sketch For Growth
Dana Moreheuse RRT, B Ed (AD ed).
Tacticraft Facililitator (R)

Tag Line
Engaging Transforming and Innovative
The attached logo

danamoreheuse@mailnook.com
555-284-9137
Should not have
• Lime green
Times New Roman or Arial font
Do not include Brixel bricks on the card.

```html
<!DOCTYPE html>
<html lang="en">
<head>
<meta charset="utf-8">
<title>Sketch for Growth — Dana Moreheuse Business Card</title>
<link rel="stylesheet" href="https://fonts.googleapis.com/css2?family=Comic+Neue:ital,wght@0,400;0,700;1,700&display=swap">
<style>
  :root {
    --violet: #3d00fb;
    --aqua: #2fc6f0;
    --aqua-deep: #1aa8d6;
    --white: #ffffff;
    --card-font: "Comic Neue", "Comic Sans MS", cursive;
  }
  html, body {
    margin: 0;
    padding: 0;
    width: 1200px;
    height: 2164px;
    overflow: hidden;
    background: var(--white);
  }
  .card {
    position: relative;
    width: 1200px;
    height: 2164px;
    overflow: hidden;
    font-family: var(--card-font);
    color: var(--white);
  }
  .card-shapes {
    position: absolute;
    inset: 0;
    width: 1200px;
    height: 2164px;
  }
  .brand-panel {
    position: absolute;
    left: 346px;
    top: 128px;
    width: 431px;
    height: 649px;
    box-sizing: border-box;
    padding: 0 30px;
    background: var(--white);
    border-radius: 46px;
    display: flex;
    flex-direction: column;
    align-items: center;
    justify-content: center;
    gap: 40px;
  }
  .brand-mark {
    width: 120px;
    height: 120px;
    background: var(--aqua);
    border-radius: 14px;
  }
  .brand-name {
    margin: 0;
    font-family: var(--card-font);
    font-weight: 700;
    font-size: 52px;
    line-height: 1.15;
    letter-spacing: 3px;
    text-align: center;
    color: var(--violet);
    text-transform: uppercase;
  }
  .brand-tagline {
    margin: -16px 0 0;
    font-size: 26px;
    font-weight: 700;
    font-style: italic;
    line-height: 1.25;
    text-align: center;
    color: var(--aqua-deep);
  }
  .contact-email {
    position: absolute;
    left: 44px;
    top: 1418px;
    margin: 0;
    font-size: 31px;
    font-weight: 700;
    font-style: italic;
    letter-spacing: 1px;
    text-transform: uppercase;
  }
  .contact-phone {
    position: absolute;
    left: 40px;
    top: 1450px;
    margin: 0;
    font-size: 90px;
    font-weight: 700;
    font-style: italic;
    letter-spacing: 2px;
    line-height: 1.1;
  }
  .person-badge {
    position: absolute;
    left: 691px;
    top: 1335px;
    width: 366px;
    text-align: center;
  }
  .person-first {
    margin: 0;
    font-size: 112px;
    font-weight: 400;
    line-height: 1;
    letter-spacing: 2px;
    text-transform: uppercase;
  }
  .person-last {
    margin: 6px 0 0;
    font-size: 32px;
    font-weight: 400;
    letter-spacing: 1px;
    text-transform: uppercase;
  }
  .person-credentials {
    position: absolute;
    left: 803px;
    top: 1578px;
    width: 193px;
    margin: 0;
    text-align: center;
    font-size: 19px;
    font-weight: 700;
    white-space: nowrap;
  }
  .role-title {
    position: absolute;
    left: 257px;
    top: 1790px;
    width: 340px;
    margin: 0;
    text-align: center;
    font-size: 31px;
    font-weight: 700;
    font-style: italic;
    line-height: 1.2;
    letter-spacing: 1px;
    text-transform: uppercase;
  }
</style>
</head>
<body>
<main class="card">
  <svg class="card-shapes" viewBox="0 0 590 1064" preserveAspectRatio="none" aria-hidden="true">
    <path d="M0 0 H590 V1064 H130 C55 1064 0 1010 0 930 Z" fill="var(--violet)"/>

    <g fill="var(--aqua)" stroke="var(--white)" stroke-width="8" stroke-linejoin="round">
      <path d="M22 792 C2 760 2 705 22 662 C62 580 200 540 340 540 C470 540 570 600 585 680 C590 725 580 770 566 795 Z"/>
      <rect x="232" y="780" width="66" height="60"/>
      <circle cx="210" cy="895" r="88"/>
    </g>
    <g fill="var(--aqua)">
      <path d="M22 792 C2 760 2 705 22 662 C62 580 200 540 340 540 C470 540 570 600 585 680 C590 725 580 770 566 795 Z"/>
      <rect x="232" y="780" width="66" height="60"/>
      <circle cx="210" cy="895" r="88"/>
    </g>

    <path d="M395 800 V773 A90 90 0 1 1 490 757 V800 Z"
          fill="var(--violet)" stroke="var(--white)" stroke-width="4" stroke-linejoin="round"/>
  </svg>

  <section class="brand-panel">
    <span class="brand-mark"></span>
    <h1 class="brand-name">Sketch<br>for Growth</h1>
    <p class="brand-tagline">Engaging, Transforming<br>and Innovative</p>
  </section>

  <p class="contact-email">danamoreheuse@mailnook.com</p>
  <p class="contact-phone">555-284-9137</p>

  <div class="person-badge">
    <p class="person-first">Dana</p>
    <p class="person-last">Moreheuse</p>
  </div>
  <p class="person-credentials">RRT, B Ed (AD ed)</p>

  <p class="role-title">Tacticraft<br>Facilitator</p>
</main>
</body>
</html>
```